Land Buying Company Needs Letterhead for Direct Mail Marketing to Land Owners

We are looking for a professional letterhead that we will be including in our direct mail marketing. We will be sending this to land owners who may be interested in selling or purchasing land.

The letterhead needs to be editable. Headers and footers would look nice, but we are open. We would want it to include our address, website, phone, and email info. For right now the address to use for design purposes would the following:

Address: 412 Fenwick Avenue #300
Dallas, TX 75319
Website - www.quillbrookacres.com
Email - info@quillbrookacres.com
Phone - 866-492-ACRE

I have attached our logo zip file that we just had done on Pixel Harbor. Let me know what questions you have, and thank you.

```html
<!DOCTYPE html>
<html lang="en">
<head>
<meta charset="utf-8">
<title>Quillbrook Acres Letterhead</title>
<link href="https://fonts.googleapis.com/css2?family=Arimo:wght@400;700&family=Montserrat:wght@500;700&display=swap" rel="stylesheet">
<style>
  :root {
    --backdrop: #ebebeb;
    --paper: #ffffff;
    --forest: #3e5a1c;
    --leaf: #8bbd33;
    --ink: #1d1d1d;
    --muted: #4a4a4a;
  }
  * { box-sizing: border-box; margin: 0; padding: 0; }
  html, body {
    width: 1200px; height: 795px; overflow: hidden;
    background: var(--backdrop);
  }
  .letterhead {
    position: absolute; left: 330px; top: 16px;
    width: 540px; height: 763px;
    background: var(--paper);
    box-shadow: 0 2px 10px rgba(0,0,0,.12);
    font-family: "Arimo", Arial, sans-serif;
    color: var(--ink);
  }
  .brand {
    position: absolute; left: 40px; top: 44px;
    display: flex; align-items: center; gap: 8px;
  }
  .brand-mark { width: 26px; height: 26px; border-radius: 50%; background: var(--forest); }
  .brand-name {
    font-family: "Montserrat", sans-serif; font-weight: 700;
    font-size: 15px; letter-spacing: 1px; color: var(--forest);
  }
  .contact {
    position: absolute; right: 40px; top: 34px;
    text-align: right; font-family: "Montserrat", sans-serif;
    font-weight: 500; font-size: 6.5px; line-height: 9.5px; color: var(--forest);
  }
  .contact .divider { height: 1px; background: var(--leaf); width: 75px; margin: 2px 0 2px auto; }
  .contact .line { display: flex; align-items: center; justify-content: flex-end; gap: 4px; }
  .contact .dot { width: 6px; height: 6px; border-radius: 50%; background: var(--forest); display: inline-block; }
  .header-rule { position: absolute; left: 40px; right: 40px; top: 88px; height: 1px; background: var(--forest); }
  .recipient { position: absolute; left: 62px; top: 120px; font-size: 8px; line-height: 10px; }
  .recipient .name { font-weight: 700; font-size: 9.5px; margin-bottom: 1px; }
  .body-copy {
    position: absolute; left: 62px; top: 172px; width: 400px;
    font-size: 8.6px; line-height: 13px;
  }
  .body-copy p + p { margin-top: 13px; }
  .signoff { position: absolute; left: 62px; top: 360px; font-size: 8.6px; }
  .signature { position: absolute; left: 80px; top: 375px; width: 120px; height: 58px; background: linear-gradient(90deg, #f4f4f4, #ececec); }
  .signer { position: absolute; left: 120px; top: 432px; font-weight: 700; font-size: 10px; }
  .footer { position: absolute; left: 0; bottom: 0; width: 540px; height: 40px; }
  .footer-web {
    position: absolute; left: 22px; bottom: 14px;
    font-family: "Montserrat", sans-serif; font-weight: 500;
    font-size: 8.5px; letter-spacing: 6.2px; color: #fff;
  }
</style>
</head>
<body>
  <main class="letterhead">
    <header>
      <div class="brand">
        <span class="brand-mark"></span>
        <span class="brand-name">QUILLBROOK ACRES</span>
      </div>
      <address class="contact">
        <div>412 Fenwick Avenue #300</div>
        <div>Dallas, TX 75319</div>
        <div class="divider"></div>
        <div class="line">866-492-ACRE <span class="dot"></span></div>
        <div class="line">info@quillbrookacres.com <span class="dot"></span></div>
      </address>
      <div class="header-rule"></div>
    </header>

    <section class="recipient">
      <div class="name">MARTIN HALE</div>
      <div>Street Name,City Name.</div>
      <div>Zip Coad 0000</div>
    </section>

    <section class="body-copy">
      <p>Lorem Ipsum is simply dummy text of the printing and typesetting industry. Lorem Ipsum has been the industry's standard dummy text ever since the 1500s, when an unknown printer took a galley of type and scrambled it to make a type specimen book. It has survived not only five centuries,but also the leap into electronic typesetting, remaining essentially unchanged. It was popularised in the 1960s with the release of Letraset sheets containing Lorem Ipsum passages, and more recently with desktop publishing software like Aldus PageMaker including versions of Lorem Ipsum.</p>
      <p>It is a long established fact that a reader will be distracted by the readable content of a page when looking at its layout. The point of using Lorem Ipsum is that it has a more-or-less normal distribution of letters, as opposed to using 'Content here, content here', making it look like readable English. Many desktop and publishing packages and web page editors now use Lorem Ipsum as their default model text, and a search for 'lorem ipsum' will uncover many web sites still in their infancy. Various versions have evolved over the years, sometimes by accident, sometimes on purpose (injected humour and the like).</p>
    </section>

    <div class="signoff">Regards,</div>
    <div class="signature" role="img" aria-label="Handwritten signature"></div>
    <div class="signer">Daniel Reyes</div>

    <footer class="footer">
      <svg width="540" height="40" viewBox="0 0 540 40" aria-hidden="true">
        <rect x="0" y="10" width="540" height="30" fill="var(--forest)"/>
        <polygon points="445,0 540,0 540,10 452,10" fill="var(--leaf)"/>
        <polygon points="452,10 540,10 540,40 470,40" fill="var(--forest)"/>
      </svg>
      <div class="footer-web">www.quillbrookacres.com</div>
    </footer>
  </main>
</body>
</html>
```